Advertising flyer for proofreading business.

Hello everyone,

I need an advertising flyer for a new proofreading company in Australia.

I would like your design in be in two sizes:
- A4 (to be posted on noticeboards),
- A6 (to be printed in larger quantity to give away)
(please see the size specification file attached).

The text file is attached (Ad Text) and it contains lots of information. Please feel free to include your choice of text from the text file, but please include Poster title, and highlight 'ESL' and students discounts.

I understand that it is impossible to include the same amount of information on A6 and A4, so please feel free to chose what fits on each of them, but please keep the design similar.

I have attached our company logo, but feel free to adjust it to the poster design (feel free to change the color as well). The original logo file contains circle around it, please feel free to remove it and include only the typeset as it can be seen here: http://www.vellumcheck.com.au/.

Flyers will be printed, so please see the specification file for details.

I will do my best to respond to feedback as soon as possible.

I appreciate your participation, time and help,
Best wishes,
Radoslaw

Target Market(s)

Students, authors

Industry/Entity Type

Business

Colors

Designer to choose colors to be used in the design.

Requirements
Must have
• It would be good if poster is easy to spot on busy noticeboards and attract attention.
• Please keep the poster in the positive/optimistic mood, and so that it focuses on students, maybe photos of graduates(?).
• Poster title,
• Please include the list of proof-read documents as they are described in the attached text file (Ad Text).
• Please highlight students discounts and ESL.
Nice to have
• I would like to leave the creative freedom to all designers so at this point I have not adjusted the Look and Feel sliders. Please feel free to offer your own take on this.
• It would be nice if most of the text could be fit to the poster.

```html
<!DOCTYPE html>
<html lang="en">
<head>
<meta charset="utf-8">
<title>Vellumcheck – Professional English language proofreading</title>
<link rel="stylesheet" href="https://fonts.googleapis.com/css2?family=Lato:wght@400;700;900&family=Roboto+Condensed:wght@700&family=Roboto:wght@400&display=swap">
<style>
  :root {
    --teal: #1fc2a2;
    --teal-deep: #17b293;
    --charcoal: #2c2f33;
    --slate: #4b4b4b;
    --ink: #2a2a2a;
    --paper: #ffffff;
    --backdrop: #e9e9e7;
  }
  * { box-sizing: border-box; margin: 0; padding: 0; }
  html, body { width: 1200px; height: 1200px; overflow: hidden; background: var(--backdrop); }
  body { font-family: "Lato", Arial, sans-serif; color: var(--ink); }
  .flyer { position: absolute; left: 136px; top: 0; width: 928px; height: 1200px; background: var(--paper); overflow: hidden; }
  .abs { position: absolute; }

  .brand-banner { left: 44px; top: 0; width: 239px; height: 190px; }
  .brand-name { left: 44px; top: 66px; width: 239px; text-align: center; color: #fff; font-weight: 700; font-size: 40px; letter-spacing: 0.5px; }

  .title { right: 44px; top: 38px; font-family: "Roboto Condensed", sans-serif; font-weight: 700; font-size: 66px; line-height: 1; color: var(--teal-deep); letter-spacing: 0.5px; }
  .subtitle { right: 44px; top: 106px; font-family: "Roboto", sans-serif; font-size: 31px; color: var(--ink); }

  .hero { left: 0; top: 150px; width: 928px; height: 333px;
    background:
      linear-gradient(to bottom, #ffffff 0%, rgba(255,255,255,0) 35%),
      linear-gradient(to right, #b8d4c4 0%, #d9e7d6 30%, #c7dbc1 60%, #a9c8a8 100%); }
  .hero::after { content: ""; position: absolute; left: 0; right: 0; bottom: 0; height: 140px;
    background: linear-gradient(to right, #8b3a4a, #6a8cb4 20%, #e0b640 40%, #c85b3a 58%, #2f5ea8 75%, #b7345a 100%); opacity: 0.55; }

  .feature-band { left: 0; top: 483px; width: 928px; height: 164px; background: var(--teal); }
  .feature-frame { left: 44px; top: 511px; width: 840px; height: 117px; border: 2px solid #fff; border-radius: 8px; }
  .feature-heading { left: 206px; top: 498px; padding: 0 8px; background: var(--teal); color: #fff; font-weight: 700; font-size: 18px; }
  .feature { color: var(--charcoal); font-weight: 700; font-size: 17px; line-height: 21px; }
  .feature .tick { position: absolute; left: -21px; top: 2px; }
  .feature-right { text-align: justify; }

  .tab { background: var(--teal); color: #fff; font-weight: 700; font-size: 20px; border-radius: 0 10px 10px 0; padding-left: 43px; line-height: 28px; }
  .tab-services { left: 0; top: 668px; width: 331px; }
  .tab-prices { left: 0; top: 786px; width: 179px; }

  .item { font-size: 15px; color: #333; white-space: nowrap; }
  .item .tick { position: absolute; left: -24px; top: 1px; }

  .testimonial { left: 0; top: 1021px; width: 928px; height: 118px; background: var(--slate); }
  .tab-testimonial { left: 378px; top: 1013px; width: 170px; height: 32px; background: var(--teal); color: #fff; font-weight: 900; font-size: 20px; letter-spacing: 1.5px; text-align: center; line-height: 32px; border-radius: 4px; }
  .quote { left: 70px; top: 1055px; width: 814px; color: #fff; font-size: 15px; line-height: 19px; }
  .qmark { color: var(--teal); font-weight: 900; font-size: 22px; }
  .q-open { left: 43px; top: 1050px; }
  .q-close { display: inline-block; margin-left: 8px; vertical-align: -6px; line-height: 0; }
  .reviewer { left: 687px; top: 1089px; font-size: 15px; line-height: 19px; color: #fff; }
  .reviewer-name { color: var(--teal); }

  .contact { left: 0; top: 1149px; width: 928px; display: flex; justify-content: center; align-items: center; gap: 14px; font-weight: 700; font-size: 16px; color: #111; }
  .contact span { display: inline-flex; align-items: center; gap: 6px; }
</style>
</head>
<body>
<svg width="0" height="0" style="position:absolute">
  <symbol id="tick" viewBox="0 0 16 16">
    <circle cx="8" cy="8" r="6.8" fill="none" stroke="currentColor" stroke-width="1.5"/>
    <path d="M4.8 8.3 L7.2 10.6 L11.3 5.6" fill="none" stroke="currentColor" stroke-width="1.7" stroke-linecap="round" stroke-linejoin="round"/>
  </symbol>
</svg>

<main class="flyer">
  <div class="hero abs" role="img" aria-label="Photo of six smiling students sitting outdoors with a laptop and tablets"></div>

  <svg class="brand-banner abs" viewBox="0 0 239 190"><polygon points="0,0 239,0 239,150 119.5,190 0,150" fill="var(--charcoal)"/></svg>
  <div class="brand-name abs">Vellumcheck</div>

  <h1 class="title abs">PROFESSIONAL</h1>
  <p class="subtitle abs">English language proofreading</p>

  <div class="feature-band abs"></div>
  <div class="feature-frame abs"></div>
  <h2 class="feature-heading abs">PROFESSIONAL, ENGLISH-LANGUAGE PROOFREADING:</h2>

  <p class="feature abs" style="left:83px;top:529px;width:360px;"><svg class="tick" width="16" height="16" style="color:#fff"><use href="#tick"/></svg>Help with English as a second language (ESL).</p>
  <p class="feature abs" style="left:83px;top:570px;width:380px;"><svg class="tick" width="16" height="16" style="color:#fff"><use href="#tick"/></svg>Proofreading by a native English speaker with an English Honours degree.</p>
  <p class="feature feature-right abs" style="left:498px;top:529px;width:369px;"><svg class="tick" width="16" height="16" style="color:#fff"><use href="#tick"/></svg>Includes correct all English language errors, spelling and grammar mistakes, reference checking and editing for style, coherence and clarity.</p>

  <h2 class="tab tab-services abs">WE WILL PROOFREAD YOUR:</h2>
  <p class="item abs" style="left:67px;top:700px;"><svg class="tick" width="16" height="16"><use href="#tick"/></svg>Essays &amp; assignments</p>
  <p class="item abs" style="left:67px;top:722px;"><svg class="tick" width="16" height="16"><use href="#tick"/></svg>Theses</p>
  <p class="item abs" style="left:67px;top:745px;"><svg class="tick" width="16" height="16"><use href="#tick"/></svg>Resumes</p>

  <p class="item abs" style="left:382px;top:671px;"><svg class="tick" width="16" height="16"><use href="#tick"/></svg>Business correspondence</p>
  <p class="item abs" style="left:382px;top:697px;"><svg class="tick" width="16" height="16"><use href="#tick"/></svg>Training manuals</p>
  <p class="item abs" style="left:382px;top:723px;"><svg class="tick" width="16" height="16"><use href="#tick"/></svg>Newsletters</p>
  <p class="item abs" style="left:382px;top:749px;"><svg class="tick" width="16" height="16"><use href="#tick"/></svg>Advertising copy</p>

  <p class="item abs" style="left:622px;top:671px;"><svg class="tick" width="16" height="16"><use href="#tick"/></svg>Brochures, catalogues &amp; media releases</p>
  <p class="item abs" style="left:622px;top:697px;"><svg class="tick" width="16" height="16"><use href="#tick"/></svg>Websites</p>
  <p class="item abs" style="left:622px;top:723px;"><svg class="tick" width="16" height="16"><use href="#tick"/></svg>Presentations &amp; speeches</p>
  <p class="item abs" style="left:622px;top:749px;"><svg class="tick" width="16" height="16"><use href="#tick"/></svg>Novels &amp; short stories</p>

  <h2 class="tab tab-prices abs">PRICE GUIDE</h2>
  <p class="item abs" style="left:67px;top:822px;"><svg class="tick" width="16" height="16"><use href="#tick"/></svg>Prices start at only $20 (short menus, flyers, letters).</p>
  <p class="item abs" style="left:67px;top:859px;"><svg class="tick" width="16" height="16"><use href="#tick"/></svg>Discounts for not-for-profit organisations and students.</p>
  <p class="item abs" style="left:67px;top:895px;"><svg class="tick" width="16" height="16"><use href="#tick"/></svg>Great student discount rate: $25 per hour (roughly 1000 words - 4 pages - of well-written text).</p>
  <p class="item abs" style="left:67px;top:931px;"><svg class="tick" width="16" height="16"><use href="#tick"/></svg>Package deals on documents over 50,000 words.</p>
  <p class="item abs" style="left:67px;top:968px;"><svg class="tick" width="16" height="16"><use href="#tick"/></svg>Fast, negotiable time-frames (same day service available by special arrangement).</p>

  <section class="testimonial abs"></section>
  <h2 class="tab-testimonial abs">TESTIMONIAL</h2>
  <span class="qmark q-open abs">&ldquo;</span>
  <p class="quote abs">Clara understood our requirements quickly and has been fantastic at delivering quality work, on time and within agreed budget. It's a pleasure to work with her.<span class="qmark q-close">&rdquo;</span></p>
  <p class="reviewer abs"><span class="reviewer-name">JOAN WHITFIELD</span><br>Operations Manager, Orbis Freight</p>

  <footer class="contact abs">
    <span>Contact us for an obligation-free quote:</span>
    <span><svg width="22" height="22" viewBox="0 0 24 24"><circle cx="12" cy="12" r="10.5" fill="none" stroke="var(--teal)" stroke-width="1.5"/><path d="M8.5 6.5c-1 1-1 3 .8 5.6 1.8 2.6 4 4.4 5.6 4.5l1.4-1.5-2-1.8-1.2.8c-1-.6-2.2-2-2.7-3.1l.9-1.1-1.5-2.3z" fill="var(--teal)"/></svg>0400 555 218</span>
    <span style="margin-left:6px"><svg width="30" height="20" viewBox="0 0 30 20"><rect x="1" y="1" width="28" height="18" rx="2" fill="none" stroke="var(--teal)" stroke-width="1.5"/><path d="M1.5 2 L15 12 L28.5 2 M1.5 18 L11 10 M28.5 18 L19 10" fill="none" stroke="var(--teal)" stroke-width="1.3"/></svg>proofing@vellumcheck.com.au</span>
  </footer>
</main>
</body>
</html>
```